Jewelry Manufacturing & Repair business needs advertising mailout - 9x4 flyer

Need new double sided flyer designed for an insert into a mailout. Want 9x4 (vertical design) to fit in 9.5" x 4.125" envelopes. Company based out of Louisiana called "Lem Tovick Manufacturing." Been in business for 45 years. We specialize in custom jewelry design and casting on the wholesale level. We are a full service trade shop offering CAD design, casting services, basic and advanced jewelry repair. Most of our customers are drawn to the fact that they talk directly with the owner/designer of the company each time they call. I've attached several images of CAD renders we've built and of our logo. I've also attached a copy of an old mailout we sent out 10 years ago that I designed myself (and it needed a lot of work). The business information listed in this old mailout is correct, except that we’ve been in business 45 years now. I would like the final design to be "business bold," portraying business strength and stability. I like shades of blue, or a gold/silver color scheme. Logo is black and white. Need double sided.

Looking for project to be less wordy than the 10 yr old mailout. Don’t need the “example scenario” in this flyer.
Updates

The weekend has made the 2 day timeframe very tight. Would like to extend timeframe, but I will select a design on Monday at 3:00 pm (USA Central time).

Target Market(s)

Retail Jewelry Stores

Industry/Entity Type

Jewelry

Colors
cfdeed
0455a3
3176b5
85acd3

Requirements
Must have
• All contact information.
Nice to have
• Purpose of this flyer is to get new accounts for our business. We want something that the retail jewelry store will notice something that will make them not throw away immediately, but instead hold onto for the future.
• This upcoming Christmas season is usually very busy for retail stores, so we can help take some of the overflow of work and still meet deadlines. With our help, they shouldn't have to turn any customer away.
Should not have
• We will be partnering in this mailout with a sister wholesale diamond company. Therefore, we don't want to mention that our company sells any diamonds, as we want to leave that part up to our sister company.

```html
<!DOCTYPE html>
<html lang="en">
<head>
<meta charset="utf-8">
<title>Lem Tovick Manufacturing – Mailout Flyer</title>
<link href="https://fonts.googleapis.com/css2?family=Montserrat:wght@400;500;700&family=Lato:ital,wght@0,400;0,700;0,900;1,900&family=Allura&display=swap" rel="stylesheet">
<style>
  :root{
    --charcoal:#3a3a3c;
    --charcoal-2:#434345;
    --backdrop-low:#e6e7e9;
    --hero-grey:#c9ced6;
    --ink:#1f1f21;
    --text:#2a2a2c;
    --white:#ffffff;
    --rule:#a9adb2;
  }
  *{margin:0;padding:0;box-sizing:border-box}
  html,body{width:1091px;height:1200px;overflow:hidden}
  body{
    position:relative;
    background:linear-gradient(to bottom,var(--charcoal) 0,var(--charcoal) 552px,var(--backdrop-low) 552px);
    font-family:'Lato',sans-serif;color:var(--text);
  }
  .side{position:absolute;box-shadow:6px 8px 14px rgba(0,0,0,.35)}

  /* front */
  .front{left:94px;top:109px;width:436px;height:981px;background:var(--white)}
  .hero{position:absolute;left:0;top:0;width:436px;height:417px;background:var(--hero-grey)}
  .brand-title{position:absolute;left:0;top:22px;width:100%;text-align:center;font-family:'Montserrat',sans-serif;color:var(--ink)}
  .brand-title .name{display:block;font-weight:700;font-size:57px;line-height:60px;letter-spacing:-.5px}
  .brand-title .sub{display:block;font-weight:400;font-size:41px;line-height:46px;letter-spacing:-.4px}
  .ring-render{position:absolute;left:40px;top:160px;width:300px;height:190px;border-radius:45%;
    background:radial-gradient(ellipse at 50% 45%,#f4f6f8 0,#c7ccd2 40%,#8d939a 68%,rgba(201,206,214,0) 72%)}
  .brand-mark{position:absolute;display:flex;align-items:center;gap:8px;font-family:'Lato',sans-serif;font-weight:900;white-space:nowrap}
  .brand-mark .dot{width:14px;height:14px;flex:none}
  .hero .brand-mark{left:300px;top:378px;font-size:18px;color:var(--ink)}
  .hero .brand-mark .dot{background:var(--ink)}
  .tagline-band{position:absolute;left:0;top:417px;width:436px;height:98px;background:var(--charcoal-2)}
  .tagline{position:absolute;left:0;top:12px;width:100%;text-align:center;font-family:'Allura',cursive;color:var(--white);font-size:35px;line-height:39px}
  .chevron{position:absolute;left:26px;top:513px}
  .pitch-title{position:absolute;left:38px;top:566px;width:360px;text-align:center;font-weight:900;font-style:italic;font-size:33px;line-height:39px;color:var(--ink);letter-spacing:-.3px}
  .pitch-body{position:absolute;left:32px;top:653px;width:378px;font-size:16.4px;line-height:20px;font-weight:700;color:#3b3b3d}
  .offer-box{position:absolute;left:18px;top:792px;width:402px;height:164px;background:var(--charcoal-2);border-radius:16px}
  .offer-box p{position:absolute;left:8px;top:14px;width:386px;text-align:center;color:var(--white);font-size:16.2px;line-height:20px;font-weight:700}
  .phone-pill{position:absolute;left:24px;top:923px;width:384px;height:48px;background:var(--white);border:2px solid var(--charcoal);border-radius:26px;
    display:flex;align-items:center;justify-content:center;font-family:'Montserrat',sans-serif;font-size:28px;font-weight:500;color:var(--ink)}

  /* back */
  .back{left:561px;top:136px;width:436px;height:954px;background:var(--charcoal-2)}
  .info{position:absolute;left:0;top:0;width:436px;height:546px;background:var(--white)}
  .info h2{position:absolute;left:29px;font-weight:400;font-size:22px;line-height:26px;color:var(--ink)}
  .info h2 b{font-weight:900;position:relative}
  .info h2 b::after{content:"";position:absolute;left:0;bottom:-6px;width:70px;height:2px;background:var(--ink);clip-path:polygon(0 0,100% 50%,0 100%)}
  .info p,.info ul{position:absolute;left:29px;width:384px;font-size:16.3px;line-height:20px;font-weight:700;color:var(--text)}
  .info ul{list-style:none}
  .info li{padding-left:19px;position:relative}
  .info li::before{content:"";position:absolute;left:2px;top:7px;width:6px;height:6px;border-radius:50%;background:var(--ink)}
  .band-photo{position:absolute;left:0;top:556px;width:436px;height:194px;
    background:radial-gradient(ellipse at 50% 55%,#d9d6d2 0,#a2846a 35%,#8a5a36 70%,#6e4426 100%)}
  .contact{position:absolute;left:0;top:750px;width:436px;height:204px}
  .contact h3{position:absolute;left:22px;top:27px;font-weight:900;font-size:25px;line-height:30px;color:var(--white);white-space:nowrap}
  .contact .details{position:absolute;left:22px;top:72px;color:var(--white);font-size:14.5px;line-height:18.6px}
  .contact .details strong{font-size:15.5px;font-weight:900}
  .contact .brand-mark{left:300px;top:112px;font-size:19px;color:var(--white)}
  .contact .brand-mark .dot{background:var(--white)}
</style>
</head>
<body>

<section class="side front">
  <div class="hero">
    <h1 class="brand-title"><span class="name">Lem Tovick</span><span class="sub">Manufacturing, LLC</span></h1>
    <div class="ring-render" role="img" aria-label="Render of an oval halo engagement ring with a twisted pavé band"></div>
    <div class="brand-mark"><span class="dot"></span>Lem Tovick</div>
  </div>
  <div class="tagline-band">
    <p class="tagline">Top Quality Craftsmanship,<br>Friendly Personal Service</p>
  </div>
  <svg class="chevron" width="384" height="18" viewBox="0 0 384 18" aria-hidden="true">
    <polygon points="0,2 384,2 384,8 200,8 192,16 184,8 0,8" fill="#a9adb2"/>
    <polygon points="0,0 384,0 384,3 0,3" fill="#434345"/>
  </svg>
  <h2 class="pitch-title">Are you looking for a way to increase profits?</h2>
  <p class="pitch-body">Recent research shows that a large percentage of customers who actively seek out a new jewelry store do so because they need some type of repair service. Additionally, customer loyalty and satisfaction are based on a store’s ability to offer a complete range of services.</p>
  <div class="offer-box">
    <p><strong>Lem Tovick Manufacturing</strong> can provide that highly skilled jeweler needed to take your business to the next level. We will work directly with you to meet all your customer’s needs, while maintaining a personal level of service that you will enjoy.</p>
  </div>
  <div class="phone-pill">Phone: 1-888-555-0142</div>
</section>

<section class="side back">
  <div class="info">
    <h2 style="top:12px"><b>Who</b> We Are:</h2>
    <p style="top:70px">We are a family operated business, serving the jewelry industry for over 45 years. Our experience provides us with a vast knowledge of the industry, as well as best practices for each unique item. We pride ourselves in quality craftsmanship with fast, honest, and courteous service.</p>
    <h2 style="top:201px"><b>What</b> We Offer:</h2>
    <ul style="top:262px">
      <li>Basic &amp; advanced jewelry repair</li>
      <li>Custom hand carved wax modeling</li>
      <li>CAD / CAM services for intricate detail</li>
      <li>Gold &amp; Platinum casting</li>
      <li>Furnish waxes, raw castings, or finished products</li>
    </ul>
    <h2 style="top:374px"><b>How</b> it works:</h2>
    <p style="top:432px">The majority of our business is done safely and securely through one of the major postal services (ParcelGo, ShipRight, NatPost). Utilizing insured overnight delivery, you have the option to have your jewelry back to you within a couple days.</p>
  </div>
  <div class="band-photo" role="img" aria-label="Photo of a stacked engagement ring and wedding band on a wooden surface"></div>
  <div class="contact">
    <h3>CALL LEM OR CORWIN TOVICK</h3>
    <p class="details"><strong>Lem Tovick Manufacturing, LLC</strong><br>12 Heron Court, Delmont, LA 71088<br>Phone: 1-888-555-0142<br>Local: 318-555-0187<br>E-mail: corwin@ltovickmfg.com</p>
    <div class="brand-mark"><span class="dot"></span>Lem Tovick</div>
  </div>
</section>

</body>
</html>
```